Briney Lark Fare landing page design

We need a landing page designed for an ecommerce website that sales fresh US domestic shrimp from the Gulf of Mexico and ships them direct to the consumer "From Our Shore To Your Door". For the landing page, we would like customers to be able to place an order and or inquire further about our product as well as links to social media. The company logo is attached

1 page

```html
<!DOCTYPE html>
<html lang="en">
<head>
<meta charset="utf-8">
<title>Briney Lark Fare — Fresh Gulf Shrimp</title>
<link href="https://fonts.googleapis.com/css2?family=Montserrat:wght@600;700&family=Poppins:wght@400;500;600;700&display=swap" rel="stylesheet">
<style>
:root{
  --orange:#ec6a3a;
  --orange-deep:#e25f2e;
  --ink:#111111;
  --text:#333333;
  --muted:#777777;
  --light:#f3f3f3;
  --line:#d6d6d6;
  --footer:#1c1c1c;
  --white:#ffffff;
}
*{margin:0;padding:0;box-sizing:border-box}
html,body{width:1200px;height:4317px;overflow:hidden;background:var(--white)}
body{font-family:"Poppins",sans-serif;color:var(--text);position:relative}
.abs{position:absolute}
h1,h2,h3{font-family:"Montserrat",sans-serif}

/* top bar */
.topbar{left:0;top:0;width:1200px;height:44px;background:var(--orange);color:var(--white);font-size:14px;font-weight:500}
.topbar .app{left:90px;top:12px;display:flex;align-items:center;gap:10px}
.topbar .login{right:94px;top:12px;display:flex;align-items:center;gap:10px}

/* header */
.header{left:0;top:44px;width:1200px;height:124px;background:var(--light)}
.brand{left:88px;top:24px;display:flex;align-items:center;gap:14px}
.brand-mark{width:96px;height:96px;border-radius:50%;border:3px solid var(--orange);background:var(--white)}
.brand-name{font-family:"Montserrat",sans-serif;font-weight:600;font-size:34px;letter-spacing:3px;color:#444;line-height:1;text-transform:uppercase;width:200px}
.nav{right:92px;top:54px;display:flex;gap:52px;font-size:16px;font-weight:500;color:var(--ink);align-items:center}
.nav .cart{display:flex;align-items:center;gap:10px}

/* hero */
.hero{left:0;top:168px;width:1200px;height:662px;background:radial-gradient(circle at 820px 330px,#c8532a 0,#8b3b1f 160px,#2e2a28 340px,#3c3b3b 560px,#2b2b2b 100%)}
.hero h1{position:absolute;left:88px;top:248px;font-size:52px;line-height:1.18;color:var(--white);font-weight:700}
.hero p{position:absolute;left:88px;top:372px;width:340px;font-size:16px;line-height:1.6;color:var(--white)}
.hero .tag{position:absolute;left:88px;top:436px;font-size:15px;font-weight:600;color:var(--white)}
.btn{display:inline-flex;align-items:center;justify-content:center;background:var(--orange);color:var(--white);font-weight:600;border-radius:30px}
.hero .btn{position:absolute;left:88px;top:482px;width:168px;height:52px;font-size:15px}

/* about */
.about h2{left:88px;top:1072px;font-size:40px;color:var(--ink)}
.about p{left:88px;top:1140px;width:540px;font-size:16px;line-height:2;color:var(--ink)}
.about .btn{left:88px;top:1374px;width:184px;height:60px;font-size:17px}
.about-frame{left:664px;top:992px;width:410px;height:20px;background:var(--orange)}
.about-frame-side{left:664px;top:992px;width:20px;height:470px;background:var(--orange)}
.about-photo{left:696px;top:1042px;width:412px;height:458px;background:linear-gradient(135deg,#f08a4a,#d9431c 50%,#f3a15e)}

/* products */
.section-title{width:1200px;left:0;text-align:center;font-size:42px;color:var(--ink)}
.product{width:240px;height:472px;top:1773px;background:var(--white);box-shadow:0 4px 14px rgba(0,0,0,.14)}
.product .photo{height:178px;position:relative}
.product .status{position:absolute;left:0;bottom:0;background:#b8461e;color:var(--white);font-size:15px;font-weight:600;padding:4px 14px}
.product h3{font-family:"Poppins",sans-serif;font-size:15px;font-weight:700;color:var(--ink);margin:40px 0 0 8px}
.product .price{margin:14px 0 0 8px;font-size:17px;font-weight:600;color:var(--ink)}
.product .price s{color:#888;font-weight:500;margin-left:18px}
.product .stars{margin:6px 0 0 8px;color:var(--orange);font-size:14px;letter-spacing:3px}
.product p{margin:12px 8px 0 8px;font-size:15px;line-height:1.6;color:var(--ink)}
.product .btn{margin:14px 0 0 8px;width:122px;height:42px;font-size:15px}
.arrow{width:48px;height:48px;border-radius:50%;background:#3a3a3a;top:1950px;display:flex;align-items:center;justify-content:center}

/* testimonials */
.quote{width:306px;height:184px;top:2584px;background:var(--white);border-radius:14px;box-shadow:0 3px 14px rgba(0,0,0,.16);padding:58px 24px 0;text-align:center;font-size:12.5px;line-height:1.85;color:#888}
.avatar{width:92px;height:92px;border-radius:50%;top:2536px;background:linear-gradient(160deg,#c9b4a2,#7a5a48);border:4px solid var(--white)}
.person{width:306px;top:2798px;text-align:center;font-size:18px;color:var(--ink);line-height:1.45}
.person span{color:var(--orange);display:block}
.person .stars{color:var(--orange);font-size:14px;letter-spacing:4px;margin-top:6px}

/* enquiry */
.enquiry-sub{left:300px;top:3116px;width:600px;text-align:center;font-size:20px;line-height:1.6;color:var(--muted)}
.field{border:2px solid var(--line);border-radius:24px;height:44px;font-size:12px;color:#777;padding:12px 18px;background:var(--white)}
.field.area{border-radius:24px;height:122px}
.submit{left:532px;top:3511px;width:136px;height:44px;border:2px solid var(--line);border-radius:24px;display:flex;align-items:center;justify-content:center;color:var(--orange);font-size:15px;font-weight:500}

/* newsletter */
.newsletter{left:0;top:3733px;width:1200px;height:141px;background:var(--orange);color:var(--white)}
.newsletter h3{position:absolute;left:166px;top:34px;font-family:"Poppins",sans-serif;font-size:26px;font-weight:600}
.newsletter p{position:absolute;left:166px;top:74px;font-size:17px}
.newsletter .input{position:absolute;left:537px;top:38px;width:404px;height:70px;background:var(--white);color:#555;font-size:16px;padding:23px 30px}
.newsletter .go{position:absolute;left:941px;top:38px;width:163px;height:70px;background:#111;color:var(--white);font-weight:600;font-size:19px;display:flex;align-items:center;justify-content:center}

/* footer */
.footer{left:0;top:3874px;width:1200px;height:443px;background:var(--footer);color:var(--white)}
.footer h4{font-size:20px;font-weight:600;position:absolute}
.footer ul{list-style:none;position:absolute;font-size:16px;line-height:32px}
.footer .row{position:absolute;display:flex;align-items:center;gap:22px;font-size:18px}
.social{position:absolute;top:298px;display:flex;gap:12px}
.social i{width:30px;height:30px;background:var(--white);border-radius:3px;display:block}
.copy{position:absolute;left:0;width:1200px;top:384px;text-align:center;font-size:16px}
</style>
</head>
<body>

<div class="abs topbar">
  <div class="abs app">
    <svg width="14" height="20" viewBox="0 0 14 20"><rect x="1" y="1" width="12" height="18" rx="2" fill="none" stroke="#fff" stroke-width="2"/></svg>
    Get the Harbor App on Your Phone
  </div>
  <div class="abs login">
    <svg width="18" height="18" viewBox="0 0 18 18"><circle cx="9" cy="5" r="4" fill="#fff"/><path d="M1 18c0-5 4-7 8-7s8 2 8 7z" fill="#fff"/></svg>
    Log In / Sign Up
  </div>
</div>

<header class="abs header">
  <div class="abs brand"><span class="brand-mark"></span><span class="brand-name">Briney Lark Fare</span></div>
  <nav class="abs nav">
    <span>Home</span><span>About</span><span>News</span><span>Shop</span><span>Contact</span>
    <span class="cart"><svg width="24" height="26" viewBox="0 0 24 26"><path d="M6 8V6a6 6 0 0 1 12 0v2" fill="none" stroke="#111" stroke-width="2"/><rect x="2" y="8" width="20" height="17" fill="#111"/></svg>Cart</span>
  </nav>
</header>

<section class="abs hero" role="img" aria-label="Cooked Gulf shrimp in a dark pan with herbs and spices">
  <h1>Welcome to<br>BRINEY LARK FARE</h1>
  <p>Lorem Ipsum is simply dummy text of the printing and typesetting industry.</p>
  <div class="tag">"From Our Shore To Your Door"</div>
  <span class="btn">Read More</span>
</section>

<section class="about">
  <h2 class="abs">About Us</h2>
  <p class="abs">Lorem Ipsum is simply dummy text of the printing and typesetting industry. Lorem Ipsum has been the industry's standard dummy text ever since the 1500s, when an unknown printer took a galley of type and scrambled it to make a type specimen book. It has survived not only five centuries, but also the leap into electronic typesetting, remaining essentially unchanged.</p>
  <span class="abs btn">Read More</span>
  <div class="abs about-frame"></div>
  <div class="abs about-frame-side"></div>
  <div class="abs about-photo" role="img" aria-label="Rows of raw orange shrimp on a board"></div>
</section>

<section class="products">
  <h2 class="abs section-title" style="top:1652px">Products</h2>
  <div class="abs arrow" style="left:22px"><svg width="14" height="14" viewBox="0 0 14 14"><path d="M9 2 4 7l5 5" fill="none" stroke="#fff" stroke-width="2.5"/></svg></div>
  <div class="abs arrow" style="left:1130px"><svg width="14" height="14" viewBox="0 0 14 14"><path d="m5 2 5 5-5 5" fill="none" stroke="#fff" stroke-width="2.5"/></svg></div>

  <article class="abs product" style="left:89px">
    <div class="photo" role="img" aria-label="Shrimp with tomato and lemon" style="background:linear-gradient(135deg,#3b6b3a,#e46a3a 50%,#b33a22)"><span class="status">AVAILABLE</span></div>
    <h3>WHITE HORSE LEG</h3><div class="price">$80.00<s>$90.00</s></div><div class="stars">★★★★★</div>
    <p>Lorem Ipsum is simply dummy text printing</p><span class="btn">Shop Now</span>
  </article>
  <article class="abs product" style="left:351px">
    <div class="photo" role="img" aria-label="Grilled shrimp on a plate with lime" style="background:linear-gradient(135deg,#2a2a2a,#c4552c 50%,#6e3b20)"><span class="status">AVAILABLE</span></div>
    <h3>WHITE HORSE LEG</h3><div class="price">$80.00<s>$90.00</s></div><div class="stars">★★★★★</div>
    <p>Lorem Ipsum is simply dummy text printing</p><span class="btn">Shop Now</span>
  </article>
  <article class="abs product" style="left:613px">
    <div class="photo" role="img" aria-label="Shrimp noodle bowl" style="background:linear-gradient(135deg,#e8d9b8,#d99a4a 50%,#7a8a4a)"><span class="status">OUT OF STOCK</span></div>
    <h3>WHITE HORSE LEG</h3><div class="price">$80.00<s>$90.00</s></div><div class="stars">★★★★★</div>
    <p>Lorem Ipsum is simply dummy text printing</p><span class="btn">Shop Now</span>
  </article>
  <article class="abs product" style="left:875px">
    <div class="photo" role="img" aria-label="Saucy shrimp in a dark bowl" style="background:linear-gradient(135deg,#1f1f1f,#d5702a 50%,#3a2a1a)"><span class="status">AVAILABLE</span></div>
    <h3>WHITE HORSE LEG</h3><div class="price">$80.00<s>$90.00</s></div><div class="stars">★★★★★</div>
    <p>Lorem Ipsum is simply dummy text printing</p><span class="btn">Shop Now</span>
  </article>
</section>

<section class="testimonials">
  <h2 class="abs section-title" style="top:2400px">Testimonials</h2>

  <div class="abs quote" style="left:100px">Sed ut perspiciatis unde omnis iste natus error sit voluptatem accantium doloremque laudantium, totam rem aperiam, eaque ipsa.</div>
  <div class="abs avatar" role="img" aria-label="Customer portrait" style="left:207px"></div>
  <div class="abs person" style="left:100px">Rana Doyle<span>USA</span><div class="stars">★★★★★</div></div>

  <div class="abs quote" style="left:447px">Sed ut perspiciatis unde omnis iste natus error sit voluptatem accantium doloremque laudantium, totam rem aperiam, eaque ipsa.</div>
  <div class="abs avatar" role="img" aria-label="Customer portrait" style="left:554px"></div>
  <div class="abs person" style="left:447px">Rana Doyle<span>USA</span><div class="stars">★★★★★</div></div>

  <div class="abs quote" style="left:794px">Sed ut perspiciatis unde omnis iste natus error sit voluptatem accantium doloremque laudantium, totam rem aperiam, eaque ipsa.</div>
  <div class="abs avatar" role="img" aria-label="Customer portrait" style="left:901px;background:linear-gradient(160deg,#d8c2a8,#2f3a55)"></div>
  <div class="abs person" style="left:794px">Rana Doyle<span>USA</span><div class="stars">★★★★★</div></div>
</section>

<section class="enquiry">
  <h2 class="abs section-title" style="top:3044px">Enquiry Form</h2>
  <p class="abs enquiry-sub">Sed ut perspiciatis unde omnis iste natus error sit voluptatem accusantium doloremque laudantium</p>
  <div class="abs field" style="left:256px;top:3217px;width:331px">Your Name</div>
  <div class="abs field" style="left:613px;top:3217px;width:331px">Your Email</div>
  <div class="abs field" style="left:256px;top:3281px;width:331px">Your Phone</div>
  <div class="abs field" style="left:613px;top:3281px;width:331px">Your Website<svg style="position:absolute;right:20px;top:18px" width="10" height="6" viewBox="0 0 10 6"><path d="M0 0h10L5 6z" fill="#888"/></svg></div>
  <div class="abs field area" style="left:256px;top:3356px;width:688px">Your Comment</div>
  <div class="abs submit">SUBMIT</div>
</section>

<section class="abs newsletter">
  <svg style="position:absolute;left:92px;top:42px" width="56" height="52" viewBox="0 0 56 52"><path d="M4 20 28 4l24 16v30H4z" fill="none" stroke="#fff" stroke-width="3"/><path d="m4 20 24 16 24-16" fill="none" stroke="#fff" stroke-width="3"/><rect x="14" y="10" width="28" height="18" fill="none" stroke="#fff" stroke-width="3"/></svg>
  <h3>Subscribe Our Newsletter</h3>
  <p>Join us for get latest updates</p>
  <div class="input">Enter your email address</div>
  <div class="go">Subscribe</div>
</section>

<footer class="abs footer">
  <h4 style="left:122px;top:58px">Contact Info</h4>
  <div class="row" style="left:118px;top:118px"><svg width="20" height="26" viewBox="0 0 20 26"><path d="M10 1a9 9 0 0 0-9 9c0 7 9 15 9 15s9-8 9-15a9 9 0 0 0-9-9z" fill="#fff"/><circle cx="10" cy="10" r="3.5" fill="#1c1c1c"/></svg>418 Pier Road, Mobile, AL</div>
  <div class="row" style="left:116px;top:186px"><svg width="26" height="24" viewBox="0 0 26 24"><path d="M3 14V11a10 10 0 0 1 20 0v3" fill="none" stroke="#fff" stroke-width="2.5"/><rect x="1" y="13" width="6" height="9" rx="2" fill="#fff"/><rect x="19" y="13" width="6" height="9" rx="2" fill="#fff"/></svg>(555) 014-2290</div>
  <div class="social" style="left:116px"><i></i><i></i><i></i><i></i></div>

  <h4 style="left:506px;top:52px">Information</h4>
  <ul style="left:506px;top:100px"><li>Home</li><li>About</li><li>News</li><li>Shop</li><li>Contact</li></ul>
  <h4 style="left:760px;top:52px">My Account</h4>
  <ul style="left:760px;top:100px"><li>Profile</li><li>Ads</li><li>FAQs</li><li>Privacy</li></ul>
  <h4 style="left:1016px;top:52px">Support</h4>
  <ul style="left:1016px;top:100px"><li>Wish List</li><li>My Account</li><li>Login</li><li>Sign Up</li><li>Wish List</li></ul>

  <div class="copy">© 2019Copyrights | Al Rights Reserved</div>
</footer>

</body>
</html>
```